Measures that matter

An internal dashboard of regular company results but with a twist!

No boring stats need apply- we want this to be visual and easy to digest for all staff on a monthly basis.

For instance, instead of a pie chat depicting the number of mobile projects won, make this a mobile charge icon ie 10 out of 50 = a fifth of charge. Or for churn rate of employees leaving the company, instead of a bar chart show 2 out of 10 people icons to show 20%.

This is built from a spreadsheet where formulas and pull throughs are already set so functionality needs to be intact.

There is one measure where there is a drop down filter, this should remain as a bar chart but be jazzed up as much as possible.

Branding elements and colours shown in the spreadsheet template, also attached is an example presentation so that you can gauge the brand tone.

Hoping for some awesome ideas here- let's show finance that design and marketing make a massive impact!

Reason: Really hoping for some clever ideas on this one so extending the deadline.

Hi Creative Minds! Really hoping to get your help on this project- a spreadsheet may seem daunting but it can be a really fun and visual project. Please let me know if you can help.

Industry/Entity Type

Marketing

Font styles to use
Other font styles liked:
• Century Gothic

```html
<!DOCTYPE html>
<html lang="en">
<head>
<meta charset="utf-8">
<title>Measures That Matter APAC – June 2014</title>
<link href="https://fonts.googleapis.com/css2?family=Poppins:wght@500;600&family=Questrial&display=swap" rel="stylesheet">
<style>
:root{
  --bg:#f0f0f0;
  --header:#505050;
  --bar:#555555;
  --bar-light:#b8b8b8;
  --hot:#ff6319;
  --orange:#f7890f;
  --orange-soft:#f9b04f;
  --white:#ffffff;
  --line:#d6d6d6;
  --ink:#333333;
  --muted:#777777;
  --green:#12b14b;
  --amber:#e9c500;
  --red:#d93a1e;
}
*{box-sizing:border-box;margin:0;padding:0}
html,body{width:1200px;height:1145px;overflow:hidden;background:var(--bg)}
body{position:relative;font-family:"Questrial",sans-serif;color:var(--ink)}
.masthead{position:absolute;left:0;top:0;width:1200px;height:58px;background:var(--header);border-bottom:2px solid #3d3d3d}
.brand{position:absolute;left:22px;top:16px;display:flex;align-items:center;gap:8px;color:var(--white);font-family:"Questrial",sans-serif;font-size:21px}
.brand-dot{width:16px;height:16px;border-radius:50%;background:var(--orange)}
.masthead h1{position:absolute;left:344px;top:12px;font-family:"Poppins",sans-serif;font-weight:600;font-size:25px;color:var(--white);letter-spacing:.2px}
.section{position:absolute;height:23px;background:var(--hot);color:var(--white);font-family:"Poppins",sans-serif;font-weight:500;font-size:17px;line-height:23px;text-align:center}
.title{position:absolute;background:var(--bar);color:var(--white);font-family:"Poppins",sans-serif;font-weight:500;font-size:14px;text-align:center;letter-spacing:.6px;display:flex;align-items:center;justify-content:center}
.title.light{background:var(--bar-light)}
.card{position:absolute;background:var(--white);border:1px solid var(--line)}
.card svg{position:absolute;left:0;top:0}
.big{font-family:"Poppins",sans-serif;font-weight:600;color:var(--orange);position:absolute}
.note{position:absolute;font-size:13px;color:var(--muted);text-align:center}
.dot{position:absolute;border-radius:50%;background:var(--green)}
svg text{font-family:"Questrial",sans-serif}
.client-table{position:absolute;left:32px;top:3px;width:408px;border-collapse:collapse;font-size:9.5px;font-family:"Poppins",sans-serif;border-left:1px solid #333;border-bottom:1px solid #333}
.client-table th{background:var(--hot);color:#222;font-weight:500;text-align:left;vertical-align:bottom;padding:0 3px;height:31px;border-right:1px solid #333;line-height:12px}
.client-table td{height:17.2px;border-bottom:1px solid #555;border-right:1px solid #333;padding:0 3px;font-family:"Questrial",sans-serif}
.client-table td.money{color:#222}
.client-table td.money span{float:right;margin-right:14px}
.client-table td.var{color:#e0001b}
.client-table td.var span{float:right;margin-right:14px}
.client-table tr.total td{background:#c9c9c9;font-family:"Poppins",sans-serif;font-weight:500}
.sale{position:absolute;left:13px;top:1038px;width:257px;height:90px;background:#f7960f;color:var(--white);text-align:center}
.sale strong{display:block;font-family:"Poppins",sans-serif;font-weight:600;font-size:50px;line-height:50px;margin-top:14px}
.sale small{display:block;font-family:"Poppins",sans-serif;font-weight:500;font-size:9.5px;margin-top:4px;letter-spacing:-.2px}
.key-row{position:absolute;left:0;width:475px;height:26px}
.key-row i{position:absolute;left:77px;top:1px;width:24px;height:24px;border-radius:50%}
.key-row span{position:absolute;left:166px;top:6px;font-size:10px;color:#333}
</style>
</head>
<body>

<header class="masthead">
  <div class="brand"><span class="brand-dot"></span>Northwind Research</div>
  <h1>MEASURES THAT MATTER APAC - June 2014</h1>
</header>

<!-- LEFT COLUMN -->
<div class="section" style="left:13px;top:77px;width:257px">THE POCKET</div>
<div class="title" style="left:13px;top:104px;width:257px;height:26px">Revenue vs Target</div>
<div class="card" style="left:13px;top:130px;width:257px;height:217px">
  <svg width="257" height="217" viewBox="0 0 257 217">
    <text x="145" y="18" font-size="9.5" fill="#f7890f">Select a BU</text>
    <text x="145" y="29" font-size="10.5" fill="#444">Total APAC</text>
    <g font-size="7.5" fill="#666" text-anchor="end">
      <text x="60" y="45">900</text><text x="60" y="60">800</text><text x="60" y="75">700</text>
      <text x="60" y="91">600</text><text x="60" y="106">500</text><text x="60" y="121">400</text>
      <text x="60" y="136">300</text><text x="60" y="151">200</text><text x="60" y="166">100</text>
      <text x="60" y="182">-</text>
    </g>
    <line x1="72" y1="42" x2="72" y2="179" stroke="#999"/>
    <rect x="89" y="86" width="24" height="93" fill="#f7890f"/>
    <rect x="149" y="57" width="24" height="122" fill="#f7890f"/>
    <rect x="209" y="159" width="24" height="20" fill="#f7890f"/>
    <g stroke="#999" fill="none">
      <line x1="72" y1="179" x2="252" y2="179"/>
      <rect x="17" y="200" width="235" height="10"/>
      <line x1="72" y1="179" x2="72" y2="210"/><line x1="132" y1="179" x2="132" y2="210"/>
      <line x1="192" y1="179" x2="192" y2="210"/><line x1="252" y1="179" x2="252" y2="210"/>
    </g>
    <g font-size="7" fill="#666" text-anchor="middle">
      <text x="102" y="188">MTD</text><text x="102" y="197">Variance</text>
      <text x="162" y="188">YTD</text><text x="162" y="197">Variance</text>
      <text x="222" y="193">FY Q2RF</text>
      <text x="102" y="208">609</text><text x="162" y="208">804</text><text x="222" y="208">134</text>
    </g>
    <rect x="19" y="203" width="5" height="5" fill="#f7890f"/>
    <text x="26" y="208" font-size="7" fill="#666">Total APAC</text>
  </svg>
</div>

<div class="title" style="left:13px;top:366px;width:257px;height:25px">Sales vs Target</div>
<div class="card" style="left:13px;top:391px;width:257px;height:190px">
  <svg width="257" height="190" viewBox="0 0 257 190">
    <text x="144" y="19" font-size="9.5" fill="#f7890f">Select a BU</text>
    <rect x="142" y="24" width="92" height="12" fill="#ededed"/>
    <text x="144" y="33" font-size="10.5" fill="#444">Total APAC</text>
    <g font-size="7.5" fill="#666" text-anchor="end">
      <text x="58" y="50">900</text><text x="58" y="61">800</text><text x="58" y="73">700</text>
      <text x="58" y="84">600</text><text x="58" y="95">500</text><text x="58" y="106">400</text>
      <text x="58" y="118">300</text><text x="58" y="129">200</text><text x="58" y="140">100</text>
      <text x="58" y="152">-</text>
    </g>
    <line x1="68" y1="47" x2="68" y2="149" stroke="#999"/>
    <rect x="84" y="80" width="24" height="69" fill="#f7890f"/>
    <rect x="141" y="58" width="24" height="91" fill="#f7890f"/>
    <rect x="199" y="134" width="24" height="15" fill="#f7890f"/>
    <g stroke="#999" fill="none">
      <line x1="68" y1="149" x2="240" y2="149"/>
      <rect x="12" y="168" width="228" height="12"/>
      <line x1="68" y1="149" x2="68" y2="180"/><line x1="125" y1="149" x2="125" y2="180"/>
      <line x1="182" y1="149" x2="182" y2="180"/><line x1="240" y1="149" x2="240" y2="180"/>
    </g>
    <g font-size="7" fill="#666" text-anchor="middle">
      <text x="96" y="157">MTD</text><text x="96" y="165">Variance</text>
      <text x="153" y="157">YTD</text><text x="153" y="165">Variance</text>
      <text x="211" y="161">FY QRF</text>
      <text x="96" y="177">609</text><text x="153" y="177">804</text><text x="211" y="177">134</text>
    </g>
    <rect x="15" y="171" width="5" height="5" fill="#f7890f"/>
    <text x="22" y="177" font-size="7" fill="#666">Total APAC</text>
  </svg>
</div>

<div class="title" style="left:13px;top:618px;width:257px;height:26px">Operating Profit vs Target (YTD)</div>
<div class="card" style="left:13px;top:644px;width:257px;height:192px">
  <svg width="257" height="192" viewBox="0 0 257 192">
    <g fill="none" transform="rotate(180 126 97)">
      <circle cx="126" cy="97" r="98" stroke="#4a4a4a" stroke-width="16" stroke-dasharray="307.9 1000"/>
      <circle cx="126" cy="97" r="73" stroke="#b0121b" stroke-width="20" stroke-dasharray="15 1000"/>
      <circle cx="126" cy="97" r="73" stroke="#e8392a" stroke-width="20" stroke-dasharray="20 1000" stroke-dashoffset="-17.8"/>
      <circle cx="126" cy="97" r="73" stroke="#f26a1b" stroke-width="20" stroke-dasharray="25 1000" stroke-dashoffset="-40.8"/>
      <circle cx="126" cy="97" r="73" stroke="#f7890f" stroke-width="20" stroke-dasharray="27 1000" stroke-dashoffset="-68.8"/>
      <circle cx="126" cy="97" r="73" stroke="#f9b04f" stroke-width="20" stroke-dasharray="133 1000" stroke-dashoffset="-98.7"/>
    </g>
    <rect x="29" y="97" width="196" height="87" fill="#8e8e8e"/>
    <polygon points="78,85 136,88 136,104" fill="#2f2f2f"/>
    <circle cx="136" cy="96" r="10" fill="#2f2f2f"/>
    <circle cx="136" cy="96" r="5" fill="#ffffff"/>
    <text x="127" y="133" text-anchor="middle" font-size="27" fill="#ffffff">-$2.4m</text>
    <text x="127" y="165" text-anchor="middle" font-size="27" fill="#ffffff">(-68%)</text>
  </svg>
</div>

<div class="title" style="left:13px;top:854px;width:257px;height:29px">APAC Provision for Doubtful</div>
<div class="card" style="left:13px;top:883px;width:257px;height:117px">
  <div class="big" style="left:22px;top:26px;font-size:48px;line-height:52px">$180k</div>
  <span class="dot" style="left:186px;top:28px;width:40px;height:40px"></span>
  <div class="note" style="left:170px;top:73px;width:80px">vs last month</div>
</div>

<div class="title" style="left:13px;top:1017px;width:257px;height:21px">June's biggest sale....</div>
<div class="sale"><strong>$50k</strong><small>SOLD BY xxxxx- PROJECT xxxx</small></div>

<!-- MIDDLE COLUMN -->
<div class="section" style="left:285px;top:79px;width:414px">THE ENGINE ROOM</div>
<div class="title" style="left:285px;top:104px;width:414px;height:27px">First-Time Right Scores (AU only)</div>
<div class="card" style="left:285px;top:131px;width:414px;height:88px">
  <div class="big" style="left:64px;top:6px;font-size:66px;line-height:76px">50%</div>
  <span class="dot" style="left:303px;top:18px;width:42px;height:42px"></span>
  <div class="note" style="left:280px;top:62px;width:90px">vs last month</div>
</div>

<div class="title" style="left:285px;top:240px;width:414px;height:26px">Panel Partner Spend</div>
<div class="card" style="left:285px;top:266px;width:414px;height:213px">
  <svg width="414" height="213" viewBox="0 0 414 213">
    <text x="296" y="25" font-size="9.5" fill="#f7890f">Select a BU</text>
    <rect x="294" y="29" width="74" height="12" fill="#ededed"/>
    <text x="296" y="39" font-size="10.5" fill="#444">Japan</text>
    <g font-size="7.5" fill="#666" text-anchor="end">
      <text x="33" y="53">0</text><text x="33" y="65">0</text><text x="33" y="77">0</text><text x="33" y="89">0</text>
      <text x="33" y="101">0</text><text x="33" y="113">0</text><text x="33" y="125">0</text><text x="33" y="137">0</text>
      <text x="33" y="149">0</text><text x="33" y="161">0</text>
    </g>
    <line x1="40" y1="158" x2="380" y2="158" stroke="#bbb"/>
    <polyline fill="none" stroke="#f7890f" stroke-width="2" points="54,63 80,128 106,133 132,114 158,119 185,128 211,130 237,125 263,145 289,146 316,157 342,124 368,164"/>
    <g fill="#ffffff" stroke="#f7890f" stroke-width="2">
      <circle cx="54" cy="63" r="4"/><circle cx="80" cy="128" r="4"/><circle cx="106" cy="133" r="4"/><circle cx="132" cy="114" r="4"/>
      <circle cx="158" cy="119" r="4"/><circle cx="185" cy="128" r="4"/><circle cx="211" cy="130" r="4"/><circle cx="237" cy="125" r="4"/>
      <circle cx="263" cy="145" r="4"/><circle cx="289" cy="146" r="4"/><circle cx="316" cy="157" r="4"/><circle cx="342" cy="124" r="4"/>
      <circle cx="368" cy="164" r="4"/>
    </g>
    <g font-size="8" fill="#666" text-anchor="end">
      <text transform="translate(58,176) rotate(-50)">Jun-13</text><text transform="translate(84,176) rotate(-50)">Jul-13</text>
      <text transform="translate(110,176) rotate(-50)">Aug-13</text><text transform="translate(136,176) rotate(-50)">Sep-13</text>
      <text transform="translate(162,176) rotate(-50)">Oct-13</text><text transform="translate(189,176) rotate(-50)">Nov-13</text>
      <text transform="translate(215,176) rotate(-50)">Dec-13</text><text transform="translate(241,176) rotate(-50)">Jan-14</text>
      <text transform="translate(267,176) rotate(-50)">Feb-14</text><text transform="translate(293,176) rotate(-50)">Mar-14</text>
      <text transform="translate(320,176) rotate(-50)">Apr-14</text><text transform="translate(346,176) rotate(-50)">May-14</text>
      <text transform="translate(372,176) rotate(-50)">Jun-14</text>
    </g>
  </svg>
</div>

<div class="title" style="left:285px;top:488px;width:414px;height:29px">THE CLASSIFIEDS</div>
<div class="card" style="left:285px;top:517px;width:414px;height:186px">
  <svg width="414" height="186" viewBox="0 0 414 186">
    <text x="207" y="20" text-anchor="middle" font-size="13" fill="#f7890f"># of Mobile Studies vs Annual Target</text>
    <rect x="34" y="63" width="140" height="63" fill="#ffffff" stroke="#111" stroke-width="2"/>
    <text x="41" y="109" font-size="36" fill="#f7890f">30/50</text>
    <rect x="171" y="62" width="212" height="84" rx="9" fill="#ffffff" stroke="#6a6a6a" stroke-width="8"/>
    <rect x="385" y="91" width="7" height="24" rx="2" fill="#6a6a6a"/>
    <g fill="#f7890f">
      <rect x="179" y="70" width="13" height="68"/><rect x="196" y="70" width="13" height="68"/><rect x="212" y="70" width="13" height="68"/>
      <rect x="229" y="70" width="13" height="68"/><rect x="246" y="70" width="13" height="68"/><rect x="263" y="70" width="13" height="68"/>
      <rect x="279" y="70" width="13" height="68"/><rect x="296" y="70" width="13" height="68"/><rect x="313" y="70" width="13" height="68"/>
      <rect x="330" y="70" width="13" height="68"/><rect x="346" y="70" width="13" height="68"/><rect x="363" y="70" width="13" height="68"/>
    </g>
  </svg>
</div>

<div class="title" style="left:285px;top:718px;width:414px;height:21px">THE TRIBE</div>
<div class="title light" style="left:285px;top:739px;width:414px;height:26px">Employee Turnover Rate</div>
<div class="card" style="left:285px;top:765px;width:414px;height:142px">
  <svg width="414" height="142" viewBox="0 0 414 142">
    <defs>
      <g id="person">
        <circle cx="13" cy="6" r="6"/>
        <rect x="3" y="14" width="20" height="28" rx="5"/>
        <rect x="-1" y="16" width="5" height="24" rx="2.5"/>
        <rect x="22" y="16" width="5" height="24" rx="2.5"/>
        <rect x="5" y="38" width="7" height="30" rx="3"/>
        <rect x="14" y="38" width="7" height="30" rx="3"/>
      </g>
    </defs>
    <g fill="#f7890f">
      <use href="#person" x="54" y="22"/><use href="#person" x="85" y="22"/><use href="#person" x="117" y="22"/><use href="#person" x="148" y="22"/>
    </g>
    <g fill="#9a9a9a">
      <use href="#person" x="180" y="22"/><use href="#person" x="211" y="22"/><use href="#person" x="243" y="22"/>
      <use href="#person" x="274" y="22"/><use href="#person" x="306" y="22"/><use href="#person" x="337" y="22"/>
    </g>
    <text x="37" y="126" font-size="11.5" fill="#f7890f">APAC 12 MONTH ROLLING CHURN RATE 44%</text>
  </svg>
</div>
<div class="title light" style="left:285px;top:907px;width:414px;height:27px">Average Annual Leave days accrued (AU only)</div>
<div class="card" style="left:285px;top:934px;width:414px;height:201px">
  <svg width="414" height="201" viewBox="0 0 414 201">
    <g font-size="8" fill="#555" text-anchor="end">
      <text x="37" y="21">15.2</text><text x="37" y="34">15</text><text x="37" y="48">14.8</text><text x="37" y="61">14.6</text>
      <text x="37" y="75">14.4</text><text x="37" y="88">14.2</text><text x="37" y="102">14</text><text x="37" y="115">13.8</text>
      <text x="37" y="129">13.6</text><text x="37" y="142">13.4</text><text x="37" y="156">13.2</text><text x="37" y="169">13</text>
    </g>
    <line x1="43" y1="166" x2="395" y2="166" stroke="#999"/>
    <polyline fill="none" stroke="#aaaaaa" stroke-width="1.2" points="73,116 132,107 191,45 250,35 308,52 366,73"/>
    <g fill="#9a9a9a">
      <ellipse cx="73" cy="116" rx="13" ry="2.5"/><ellipse cx="132" cy="107" rx="13" ry="2.5"/><ellipse cx="191" cy="45" rx="13" ry="2.5"/>
      <ellipse cx="250" cy="35" rx="13" ry="2.5"/><ellipse cx="308" cy="52" rx="13" ry="2.5"/><ellipse cx="366" cy="73" rx="13" ry="2.5"/>
    </g>
    <g font-size="8.5" fill="#555" text-anchor="middle">
      <text x="73" y="185">Jan-14</text><text x="132" y="185">Feb-14</text><text x="191" y="185">Mar-14</text>
      <text x="250" y="185">Apr-14</text><text x="308" y="185">May-14</text><text x="366" y="185">Jun-14</text>
    </g>
  </svg>
</div>

<!-- RIGHT COLUMN -->
<div class="section" style="left:720px;top:79px;width:475px">THE CHOSEN ONES</div>
<div class="title" style="left:720px;top:104px;width:475px;height:20px">Average CSAT Result (YTD)</div>
<div class="card" style="left:720px;top:127px;width:475px;height:226px"></div>

<div class="title" style="left:720px;top:365px;width:475px;height:32px">APAC Client Analysis (YTD)</div>
<div class="card" style="left:720px;top:397px;width:475px;height:278px">
  <table class="client-table">
    <colgroup><col style="width:192px"><col style="width:75px"><col style="width:64px"><col style="width:77px"></colgroup>
    <thead><tr><th>Client</th><th>Revenue<br>($'000's)</th><th>Variance to<br>Target</th><th>GM %<br>(target xx%)</th></tr></thead>
    <tbody>
      <tr><td>xx</td><td class="money">$<span>-</span></td><td class="var">$<span>-</span></td><td></td></tr>
      <tr><td>xx</td><td class="money">$<span>-</span></td><td class="var">$<span>-</span></td><td></td></tr>
      <tr><td>xx</td><td class="money">$<span>-</span></td><td class="var">$<span>-</span></td><td></td></tr>
      <tr><td>xx</td><td class="money">$<span>-</span></td><td class="var">$<span>-</span></td><td></td></tr>
      <tr><td>xx</td><td class="money">$<span>-</span></td><td class="var">$<span>-</span></td><td></td></tr>
      <tr><td>xx</td><td class="money">$<span>-</span></td><td class="var">$<span>-</span></td><td></td></tr>
      <tr><td>xx</td><td class="money">$<span>-</span></td><td class="var">$<span>-</span></td><td></td></tr>
      <tr><td>xx</td><td class="money">$<span>-</span></td><td class="var">$<span>-</span></td><td></td></tr>
      <tr><td>xx</td><td class="money">$<span>-</span></td><td class="var">$<span>-</span></td><td></td></tr>
      <tr><td>xx</td><td class="money">$<span>-</span></td><td class="var">$<span>-</span></td><td></td></tr>
      <tr><td>xx</td><td class="money">$<span>-</span></td><td class="var">$<span>-</span></td><td></td></tr>
      <tr class="total"><td>Total APAC</td><td></td><td></td><td></td></tr>
    </tbody>
  </table>
</div>

<div class="section" style="left:720px;top:692px;width:475px;height:20px;line-height:20px">PANEL HEALTH</div>
<div class="title" style="left:720px;top:716px;width:475px;height:22px">Panel Size &amp; Respondents</div>
<div class="card" style="left:720px;top:738px;width:475px;height:262px">
  <svg width="475" height="262" viewBox="0 0 475 262">
    <g font-size="10" fill="#333" text-anchor="middle">
      <text x="145" y="14">Select a panel (size)</text><text x="145" y="26">Global Panel Size</text>
      <text x="300" y="14">Select a panel (Responders)</text><text x="300" y="26">GLOBAL RESPONDERS</text>
    </g>
    <g font-size="7.5" fill="#666" text-anchor="end">
      <text x="29" y="54">900</text><text x="29" y="72">800</text><text x="29" y="90">700</text><text x="29" y="108">600</text>
      <text x="29" y="126">500</text><text x="29" y="144">400</text><text x="29" y="162">300</text><text x="29" y="180">200</text>
      <text x="29" y="198">100</text>
    </g>
    <line x1="39" y1="50" x2="39" y2="212" stroke="#999"/>
    <line x1="39" y1="212" x2="440" y2="212" stroke="#999"/>
    <polyline fill="none" stroke="#b5b5b5" stroke-width="2" points="55,75 89,75 122,75 156,75 190,75 223,75 257,75 291,75 324,75 358,75 392,75 426,75"/>
    <g fill="#b5b5b5">
      <circle cx="55" cy="75" r="5"/><circle cx="89" cy="75" r="5"/><circle cx="122" cy="75" r="5"/><circle cx="156" cy="75" r="5"/>
      <circle cx="190" cy="75" r="5"/><circle cx="223" cy="75" r="5"/><circle cx="257" cy="75" r="5"/><circle cx="291" cy="75" r="5"/>
      <circle cx="324" cy="75" r="5"/><circle cx="358" cy="75" r="5"/><circle cx="392" cy="75" r="5"/><circle cx="426" cy="75" r="5"/>
    </g>
    <polyline fill="none" stroke="#ff5a1f" stroke-width="2" points="55,144 89,144 122,144 156,144 190,144 223,144 257,144 291,144 324,144 358,144 392,144 426,144"/>
    <g fill="#ff5a1f">
      <rect x="51" y="140" width="8" height="8"/><rect x="85" y="140" width="8" height="8"/><rect x="118" y="140" width="8" height="8"/>
      <rect x="152" y="140" width="8" height="8"/><rect x="186" y="140" width="8" height="8"/><rect x="219" y="140" width="8" height="8"/>
      <rect x="253" y="140" width="8" height="8"/><rect x="287" y="140" width="8" height="8"/><rect x="320" y="140" width="8" height="8"/>
      <rect x="354" y="140" width="8" height="8"/><rect x="388" y="140" width="8" height="8"/><rect x="422" y="140" width="8" height="8"/>
    </g>
    <g font-size="7.5" fill="#666" text-anchor="middle">
      <text x="55" y="224">Jul-13</text><text x="89" y="224">Aug-13</text><text x="122" y="224">Sep-13</text><text x="156" y="224">Oct-13</text>
      <text x="190" y="224">Nov-13</text><text x="223" y="224">Dec-13</text><text x="257" y="224">Jan-14</text><text x="291" y="224">Feb-14</text>
      <text x="324" y="224">Mar-14</text><text x="358" y="224">Apr-14</text><text x="392" y="224">May-14</text><text x="426" y="224">Jun-14</text>
    </g>
    <line x1="150" y1="237" x2="164" y2="237" stroke="#b5b5b5" stroke-width="2"/><circle cx="157" cy="237" r="3" fill="#b5b5b5"/>
    <text x="166" y="240" font-size="6.5" fill="#666">Global Panel Size</text>
    <line x1="236" y1="237" x2="250" y2="237" stroke="#ff5a1f" stroke-width="2"/><rect x="240" y="234" width="6" height="6" fill="#ff5a1f"/>
    <text x="252" y="240" font-size="6.5" fill="#666">GLOBAL RESPONDERS</text>
  </svg>
</div>

<div class="title" style="left:720px;top:1014px;width:475px;height:25px">Key&gt;&gt;</div>
<div class="card" style="left:720px;top:1039px;width:475px;height:96px">
  <div class="key-row" style="top:10px"><i style="background:var(--green)"></i><span>Budget/Prior month result achieved/exceeded</span></div>
  <div class="key-row" style="top:36px"><i style="background:var(--amber)"></i><span>Adverse variance (between 1% &amp; 10%) to the budget/prior month.</span></div>
  <div class="key-row" style="top:61px"><i style="background:var(--red)"></i><span>&gt;10% adverse variance to the budget/prior month.</span></div>
</div>

</body>
</html>
```